Flyer Design

Create a flyer using the logo theme. Single page for to be sent out on email. Attached is an image of the layout, below is the text. A5 and a4 versions.

Simplifying the MAZE

This short workshop is designed as a refresher for those surgeons who have attended a full Cox-MAZE training course, and wish to gain an update on the latest thinking with regards to the surgical treatment of Atrial Fibrillation.
We will start with an overview of the disease burden, talk to the foundation clinical evidence available, and cover the various lesion sets used by surgeons – with a view to simplifying the procedure. The workshop will also explain the technology used, how to treat the Left Atrial Appendage, the best ways to work with your EP colleagues, and involve a short hands-on session to familiarize you with the tools available to perform the Cox-MAZE procedure.

Faculty
{{image}}
Mr. Corwen Halse
Cardiothoracic Surgeon

Mr Halses training was completed at the Brannock Clinic, Rochester, Minnesota, between June 1995 and July 1997 followed by an advanced fellowship with Professor Osric J Talmane at the Westvale General Hospital. Additional expertise required visits to Belgium, Italy, England and the United States. Mr Halse now proctors internationally in order to share his knowledge and further improvement in all areas of minimal access and open cardiac and thoracic surgery.
Further overseas experience at the Westvale General Hospital in Canada culminated in the award of Clinical Fellowship in Cardiovascular Surgery in December 1997.

Mr Halse has contributed to many publications and is referee for Journal articles in very highly regarded professional journals. He performs both Cardiac surgery procedures and thoracic procedures at Harrowgate Private Hospital and Venholt Hospital, Melbourne. Mr Halse has performed in excess of 200 open Maze procedures and 35 via a Thoracoscopic approach.

Venue - TBA
Time : 5pm - 7.30pm, followed by dinner and case presentations

```html
<!DOCTYPE html>
<html lang="en">
<head>
<meta charset="utf-8">
<title>Simplifying the MAZE – Workshop Flyer</title>
<link rel="stylesheet" href="https://fonts.googleapis.com/css2?family=Fira+Sans:ital,wght@0,400;0,500;0,600;0,700;0,800;1,300;1,400;1,500&family=PT+Serif:ital,wght@0,400;0,700;1,400&family=Raleway:wght@200&family=Roboto+Condensed:wght@700&display=swap">
<style>
  :root {
    --page-frame: #e6e7e8;
    --paper: #ffffff;
    --blue-deep: #0a55a3;
    --blue-mid: #0b7fd0;
    --blue-bright: #10b4ee;
    --navy-ink: #14233f;
    --name-blue: #2b7fc1;
    --event-blue: #1557a8;
    --ink: #1f1f1f;
    --ink-soft: #333333;
    --rule: #c9c9c9;
    --photo-dark: #2a2a2c;
    --photo-mid: #5a5856;
  }
  * { box-sizing: border-box; margin: 0; padding: 0; }
  html, body { width: 862px; height: 1200px; overflow: hidden; background: var(--page-frame); }
  .flyer { position: relative; width: 862px; height: 1200px; background: var(--page-frame); }
  .sheet { position: absolute; left: 14px; top: 14px; right: 14px; bottom: 50px; background: var(--paper); }
  .hero {
    position: absolute; left: 46px; top: 46px; width: 768px; height: 418px;
    background: radial-gradient(ellipse 70% 75% at 50% 45%, var(--blue-bright) 0%, var(--blue-mid) 48%, var(--blue-deep) 100%);
    color: #fff; text-align: center;
  }
  .hero__title {
    font-family: "Fira Sans", sans-serif; font-weight: 800;
    font-size: 64px; letter-spacing: 0.5px; line-height: 1;
    margin-top: 36px;
    text-shadow: 0 3px 4px rgba(0,0,0,0.35);
  }
  .hero__lead {
    font-family: "Fira Sans", sans-serif; font-weight: 600;
    font-size: 20.5px; line-height: 27px;
    width: 620px; margin: 38px auto 0;
  }
  .hero__body {
    font-family: "PT Serif", serif; font-size: 12.2px; line-height: 19.2px;
    color: var(--navy-ink); white-space: nowrap;
    margin: 38px auto 0; width: 740px;
  }
  .hero__body b { font-weight: 700; }
  .hero__body .opening { font-style: italic; font-size: 15px; }
  .faculty-heading {
    position: absolute; left: 0; right: 0; top: 477px; text-align: center;
    font-family: "Raleway", sans-serif; font-weight: 200;
    font-size: 78px; letter-spacing: 1px; color: #111;
  }
  .faculty__photo {
    position: absolute; left: 57px; top: 594px; width: 227px; height: 308px;
    background: radial-gradient(ellipse 60% 50% at 50% 35%, var(--photo-mid), var(--photo-dark));
  }
  .faculty__name {
    position: absolute; left: 40px; width: 262px; top: 912px; text-align: center;
    font-family: "Fira Sans", sans-serif; font-weight: 500;
    font-size: 23px; letter-spacing: 0.6px; color: var(--name-blue); text-transform: uppercase;
  }
  .faculty__role {
    position: absolute; left: 40px; width: 262px; top: 945px; text-align: center;
    font-family: "Fira Sans", sans-serif; font-style: italic; font-weight: 500;
    font-size: 16.5px; color: var(--ink);
  }
  .faculty__bio {
    position: absolute; left: 328px; top: 590px; width: 468px;
    font-family: "Fira Sans", sans-serif; font-style: italic; font-weight: 400;
    font-size: 14.6px; line-height: 21.8px; color: var(--ink);
    text-align: justify;
  }
  .faculty__bio p + p { margin-top: 10.5px; }
  .brand {
    position: absolute; left: 58px; top: 1038px; width: 334px;
    display: flex; flex-direction: column; align-items: center;
  }
  .brand__name {
    font-family: "Fira Sans", sans-serif; font-weight: 600;
    font-size: 62px; line-height: 1; color: var(--ink-soft);
  }
  .brand__region {
    margin-top: 14px;
    font-family: "Fira Sans", sans-serif; font-weight: 600;
    font-size: 12.5px; letter-spacing: 0.2px; color: var(--ink-soft);
  }
  .divider { position: absolute; left: 419px; top: 1030px; width: 1px; height: 104px; background: var(--rule); }
  .event {
    position: absolute; left: 447px; top: 1026px;
    font-family: "Roboto Condensed", sans-serif; font-weight: 700;
    color: var(--event-blue); text-transform: uppercase;
  }
  .event__line { font-size: 36px; line-height: 37px; letter-spacing: 0.3px; }
  .event__note {
    margin-top: 14px;
    font-family: "Fira Sans", sans-serif; font-weight: 600;
    font-size: 17.5px; color: var(--ink-soft); text-transform: none;
  }
</style>
</head>
<body>
<main class="flyer">
  <div class="sheet"></div>

  <section class="hero">
    <h1 class="hero__title">Simplifying the MAZE</h1>
    <p class="hero__lead">This SHORT WORKSHOP is designed as a refresher for those surgeons who have attended a full Cox-MAZE training course, and wish to gain an update on the latest thinking with regards to the surgical treatment of Atrial Fibrillation.</p>
    <p class="hero__body"><span class="opening">We will start with an</span> overview of the <b>disease burden</b>, talk to the <b>foundation clinical evidence</b><br><b>available</b>, and cover the <b>various lesion sets used by surgeons</b> – with a view to simplifying the procedure.<br>The workshop will also <b>explain the technology used</b>, <b>how to treat the Left Atrial Appendage</b>,<br>the <b>best ways to work with your EP colleagues</b>, and involve a short hands-on<br>session to familiarize you with the tools available to<br>perform the Cox-MAZE procedure.</p>
  </section>

  <h2 class="faculty-heading">FACULTY</h2>

  <div class="faculty__photo" role="img" aria-label="Portrait photograph of Mr Corwen Halse, cardiothoracic surgeon, in a dark suit"></div>
  <p class="faculty__name">Mr. Corwen Halse</p>
  <p class="faculty__role">Cardiothoracic Surgeon</p>

  <div class="faculty__bio">
    <p>Mr Halses training was completed at the Brannock Clinic, Rochester, Minnesota, between June 1995 and July 1997 followed by an advanced fellowship with Professor Osric J Talmane at the Westvale General Hospital. Additional expertise required visits to Belgium, Italy, England and the United States. Mr Halse now proctors internationally in order to share his knowledge and further improvement in all areas of minimal access and open cardiac and thoracic surgery.</p>
    <p>Further overseas experience at the Westvale General Hospital in Canada culminated in the award of Clinical Fellowship in Cardiovascular Surgery in December 1997.</p>
    <p>Mr Halse has contributed to many publications and is referee for Journal articles in very highly regarded professional journals. He performs both Cardiac surgery procedures and thoracic procedures at Harrowgate Private Hospital and Venholt Hospital, Melbourne. Mr Halse has performed in excess of 200 open Maze procedures and 35 via a Thoracoscopic approach.</p>
  </div>

  <div class="brand">
    <span class="brand__name">Veltrane</span>
    <span class="brand__region">AUSTRALIA AND NEW ZEALAND</span>
  </div>

  <div class="divider"></div>

  <div class="event">
    <p class="event__line">Venue:&nbsp; TBA</p>
    <p class="event__line">Time: 5pm-7.30pm</p>
    <p class="event__note">Followed By Dinner And Case Presentations</p>
  </div>
</main>
</body>
</html>
```